Conceptual Model Diagram for Replacing Medication with Behavior to Support Weight Loss Maintenance

Design a figure of a conceptual model that needs to be inserted into a word document for a PSF grant. This conceptual model illustrates how behavioral strategies can replace the regulatory functions lost after AOM discontinuation. The intervention targets three core vulnerabilities—appetite resurgence, metabolic inflexibility, and suboptimal mindstate—through the domains of Food, Physical Activity, and Mind. Sustained weight loss maintenance occurs at the intersection of these domains. The intervention is delivered within a design framework that makes behaviors easier to perform, aligns them with identity, and reinforces them through virtual support and community, ensuring real-world feasibility and long-term adherence.
Target Market(s)
PSF reviewers
Industry/Entity Type
academic
Other font styles liked:
- arial
Requirements
Must have
- see my attached description

```html
<!DOCTYPE html>
<html lang="en">
<head>
<meta charset="utf-8">
<title>Conceptual Model – Behavior-Based Weight Loss Maintenance</title>
<link rel="stylesheet" href="https://fonts.googleapis.com/css2?family=Barlow+Semi+Condensed:wght@500;600&family=Poppins:wght@300;600&display=swap">
<style>
  :root {
    --paper: #ffffff;
    --ink: #2b2b2b;
    --line: #3a3a3a;
    --ring-line: #4a4a4a;
  }
  html, body {
    margin: 0;
    padding: 0;
    width: 1200px;
    height: 1199px;
    overflow: hidden;
    background: var(--paper);
  }
  .model {
    display: block;
    width: 1200px;
    height: 1199px;
  }
  .ring { fill: none; stroke: var(--ring-line); stroke-width: 1.2; }
  .domain { fill: none; stroke: var(--line); stroke-width: 2; }
  .ring-text {
    font-family: "Poppins", Arial, sans-serif;
    font-weight: 300;
    font-size: 20px;
    fill: var(--ink);
  }
  .ring-text .dash { font-weight: 600; }
  .domain-label {
    font-family: "Barlow Semi Condensed", Arial, sans-serif;
    font-weight: 600;
    font-size: 21px;
    fill: var(--ink);
    text-anchor: middle;
  }
  .outcome-label {
    font-family: "Barlow Semi Condensed", Arial, sans-serif;
    font-weight: 600;
    font-size: 15.5px;
    fill: var(--ink);
    text-anchor: middle;
  }
  .vulnerability {
    font-family: "Barlow Semi Condensed", Arial, sans-serif;
    font-weight: 600;
    font-size: 14px;
    fill: var(--ink);
    text-anchor: middle;
  }
  .pointer { stroke: var(--line); stroke-width: 1.2; fill: none; }
  .pointer-head { fill: var(--line); }
</style>
</head>
<body>
<svg class="model" viewBox="0 0 1440 1439" preserveAspectRatio="none" role="img" aria-label="Conceptual model: Food, Physical Activity and Mind overlap in Sustained Weight Loss Maintenance, surrounded by design framework rings">
  <defs>
    <marker id="arrowhead" viewBox="0 0 10 10" refX="9" refY="5" markerWidth="8" markerHeight="8" orient="auto-start-reverse">
      <path class="pointer-head" d="M0,1 L10,5 L0,9 Z"/>
    </marker>
    <path id="path-identity" d="M 309,715 A 407 407 0 1 1 1123,715 A 407 407 0 1 1 309,715"/>
    <path id="path-easy" d="M 1074,715 A 358 358 0 1 1 358,715 A 358 358 0 1 1 1074,715"/>
    <path id="path-support" d="M 248,715 A 468 468 0 1 0 1184,715 A 468 468 0 1 0 248,715"/>
  </defs>

  <g class="framework-rings">
    <circle class="ring" cx="716" cy="715" r="487"/>
    <circle class="ring" cx="716" cy="715" r="440"/>
    <circle class="ring" cx="716" cy="715" r="393"/>
    <circle class="ring" cx="716" cy="715" r="345"/>
  </g>

  <g class="framework-labels">
    <text class="ring-text">
      <textPath href="#path-identity" startOffset="547" textLength="648" lengthAdjust="spacing">Align with Identity <tspan class="dash">–</tspan> self-concept, Sustain ON model, internalization</textPath>
    </text>
    <text class="ring-text">
      <textPath href="#path-easy" startOffset="937" textLength="530" lengthAdjust="spacing">Make it Easy <tspan class="dash">–</tspan> habits, routines, environment, low friction</textPath>
    </text>
    <text class="ring-text">
      <textPath href="#path-support" startOffset="621" textLength="880" lengthAdjust="spacing">Virtual Support and Social Connection <tspan class="dash">–</tspan> accessibility, community, shared accountability</textPath>
    </text>
  </g>

  <g class="domains">
    <circle class="domain" cx="621" cy="660" r="168"/>
    <circle class="domain" cx="812" cy="660" r="168"/>
    <circle class="domain" cx="711" cy="814" r="168"/>
  </g>

  <text class="domain-label" x="568" y="618">Food</text>
  <text class="domain-label" x="860" y="615">Physical</text>
  <text class="domain-label" x="860" y="643">Activity</text>
  <text class="domain-label" x="715" y="904">Mind</text>

  <g class="outcome">
    <text class="outcome-label" x="717" y="691">Sustained</text>
    <text class="outcome-label" x="717" y="711">Weight Loss</text>
    <text class="outcome-label" x="717" y="731">Maintenance</text>
  </g>

  <text class="vulnerability" transform="translate(506,512) rotate(-32)">Appetite Resurgence</text>
  <line class="pointer" x1="516" y1="526" x2="549" y2="589" marker-end="url(#arrowhead)"/>

  <text class="vulnerability" transform="translate(940,514) rotate(46)">Metabolic Inflexibility</text>
  <line class="pointer" x1="926" y1="530" x2="884" y2="590" marker-end="url(#arrowhead)"/>

  <text class="vulnerability" transform="translate(719,1010) rotate(-3)">Suboptimal Mindstate</text>
  <line class="pointer" x1="714" y1="995" x2="714" y2="917" marker-end="url(#arrowhead)"/>
</svg>
</body>
</html>
```